Dorvelan Swimming & Athletics Center

We need Business Card for a Athletics center
The logo frome the Uploaded Files ( b card fimal)
Οn one side of card we need the logo of company the Contact and the website:
1. Address:(Limassol, Cyprus 12-14 Stavrinelou str,Ano Trimeni,P.C. 4832)

2.Phone number: (+357) 25-704263

3. Mail: info@dorvelanfit.example

3. Website: www.dorvelanfit.example

Οn the other side of the card we need to write the sport of the company:

1. Artistic Gymnastics
2. Swimming
3. Gym - Fitness
4. Programs
5. Dancing
5.Tennis

From the Uploaded Files you can get the logo.In a logo is behind the black color which can be removed from logo.

Υou can use that color you want.
.
Updates

Industry/Entity Type

Business

Font styles to use
Decorative

Colors
0555a3
ffcf3e
3176b5
0692cd
add136
f04a50
000000
cfcfcf
9d9d9d

Requirements
Should not have
• photos with faces
• photo fro the Website:www.dorvelanfit.example

```html
<!DOCTYPE html>
<html lang="en">
<head>
<meta charset="utf-8">
<title>Dorvelan Swimming &amp; Athletics Center — Business Card</title>
<link rel="stylesheet" href="https://fonts.googleapis.com/css2?family=Montserrat:wght@400;500;700;900&display=swap">
<style>
  :root {
    --backdrop: #2b2b2d;
    --card: #1d1e21;
    --gold: #f6b21c;
    --gold-soft: #ffcf3e;
    --ink: #f4f4f4;
    --rule: #cfcfcf;
  }
  * { box-sizing: border-box; margin: 0; padding: 0; }
  html, body { width: 1200px; height: 1189px; overflow: hidden; }
  body {
    background: var(--backdrop);
    font-family: "Montserrat", sans-serif;
    color: var(--ink);
    position: relative;
  }
  .card {
    position: absolute;
    left: 160px;
    width: 880px;
    height: 503px;
    background: var(--card);
    border-radius: 26px;
    box-shadow: 0 18px 40px rgba(0,0,0,.45);
    overflow: hidden;
  }
  .card--front { top: 64px; }
  .card--back { top: 622px; }

  /* Brand lockup */
  .brand {
    position: absolute;
    display: flex;
    align-items: center;
    gap: 22px;
  }
  .brand__name {
    font-weight: 900;
    color: var(--gold);
    letter-spacing: 2px;
    line-height: 1;
    white-space: nowrap;
  }
  .brand__mark {
    border: 3px solid var(--gold);
    border-radius: 50%;
    flex: none;
  }

  /* Front side */
  .card--front .brand { left: 120px; top: 150px; }
  .card--front .brand__name { font-size: 86px; }
  .card--front .brand__mark { width: 92px; height: 92px; }

  .services {
    position: absolute;
    left: 130px;
    top: 282px;
    font-size: 24px;
    font-weight: 500;
    letter-spacing: 1px;
    line-height: 1.6;
    text-transform: uppercase;
    white-space: nowrap;
  }
  .services__line:first-child { padding-left: 76px; }

  /* Back side */
  .card--back .brand { right: 90px; top: 84px; }
  .card--back .brand__name { font-size: 92px; }

  .holder {
    position: absolute;
    left: 318px;
    top: 210px;
    text-align: right;
    width: 262px;
  }
  .holder__name {
    color: var(--gold);
    font-weight: 700;
    font-size: 30px;
    letter-spacing: 1px;
    white-space: nowrap;
  }
  .holder__role { font-size: 22px; font-weight: 500; margin-top: 2px; }

  .rule {
    position: absolute;
    height: 2px;
    background: var(--rule);
    top: 244px;
  }
  .rule--left { left: 0; width: 300px; }
  .rule--right { left: 600px; right: 0; }

  .address {
    position: absolute;
    right: 470px;
    top: 296px;
    text-align: right;
    font-size: 22px;
    font-style: normal;
    font-weight: 500;
    line-height: 1.55;
    white-space: nowrap;
  }
  .divider {
    position: absolute;
    left: 430px;
    top: 290px;
    width: 2px;
    height: 118px;
    background: var(--gold);
  }
  .contacts {
    position: absolute;
    left: 452px;
    top: 290px;
    list-style: none;
    font-size: 22px;
    font-weight: 500;
    white-space: nowrap;
  }
  .contacts__item {
    display: flex;
    align-items: center;
    gap: 14px;
    height: 40px;
  }
  .contacts__icon {
    width: 30px;
    height: 30px;
    border-radius: 5px;
    background: var(--gold-soft);
    display: grid;
    place-items: center;
    flex: none;
  }
</style>
</head>
<body>

<section class="card card--front" aria-label="Card front">
  <div class="brand">
    <span class="brand__name">DORVELAN</span>
    <span class="brand__mark"></span>
  </div>
  <div class="services">
    <p class="services__line">Artistic Gymnastics | Swimming</p>
    <p class="services__line">Gym - Fitness | Programs | Dancing | Tennis</p>
  </div>
</section>

<section class="card card--back" aria-label="Card back">
  <div class="brand">
    <span class="brand__name">DORVELAN</span>
  </div>

  <div class="rule rule--left"></div>
  <div class="rule rule--right"></div>

  <div class="holder">
    <p class="holder__name">MARO KELLIS</p>
    <p class="holder__role">Owner</p>
  </div>

  <address class="address">
    Limassol,<br>
    Cyprus 12-14 Stavrinelou str,<br>
    Ano Trimeni,P.C. 4832
  </address>

  <div class="divider"></div>

  <ul class="contacts">
    <li class="contacts__item">
      <span class="contacts__icon">
        <svg width="18" height="18" viewBox="0 0 24 24" aria-hidden="true"><path fill="#1d1e21" d="M6.6 10.8a15.1 15.1 0 0 0 6.6 6.6l2.2-2.2a1 1 0 0 1 1-.25 11.4 11.4 0 0 0 3.6.57 1 1 0 0 1 1 1V20a1 1 0 0 1-1 1A17 17 0 0 1 3 4a1 1 0 0 1 1-1h3.5a1 1 0 0 1 1 1c0 1.25.2 2.450.57 3.57a1 1 0 0 1-.25 1z"/></svg>
      </span>
      (+357) 25-704263
    </li>
    <li class="contacts__item">
      <span class="contacts__icon">
        <svg width="20" height="16" viewBox="0 0 24 18" aria-hidden="true"><rect x="1" y="1" width="22" height="16" rx="1.5" fill="none" stroke="#1d1e21" stroke-width="2"/><path d="M1 2l11 8 11-8" fill="none" stroke="#1d1e21" stroke-width="2"/></svg>
      </span>
      info@dorvelanfit.example
    </li>
    <li class="contacts__item">
      <span class="contacts__icon">
        <svg width="20" height="20" viewBox="0 0 24 24" aria-hidden="true" fill="none" stroke="#1d1e21" stroke-width="1.8"><circle cx="12" cy="12" r="10"/><ellipse cx="12" cy="12" rx="4.5" ry="10"/><path d="M2 12h20M4 6.5h16M4 17.5h16"/></svg>
      </span>
      www.dorvelanfit.example
    </li>
  </ul>
</section>

</body>
</html>
```